Webbanner-Design für Dienstleistung der Onlineshop-Betreuung
Zielgruppe
kalVorn ist eine moderne IT-Beratung mit Fokus auf IT-Consulting und Software-Entwicklung. Unser Haupt-Klientel lässt sich in 3 Branchen Unterteilen:
1) Onlineshop-Betreiber (auch künftige)
2) Service Provider für E-Commerce (Zahlungsanbieter, Logistiker, etc.)
3) Allgemeine Online Plattformen (individuelle Software)
Wir entwickeln für unsere Kunden Online Shops, Module und Plugins für Shop- und Warenwirtschaftssysteme, so wie individuelle Software nach Kundenwunsch bzw. -bedarf. Darüberhinaus betreuen wir Onlineshops und übernehmen je nach Kundenwunsch von der Administration über die Pflege bis zur Optimierung und Weiterentwicklung alle Aufgaben.
Siehe auch https://www.kalvorn-beispiel.de/unternehmen/
bzw. https://www.kalvorn-beispiel.de/leistungen/
Aufgabenstellung
Das Banner wird in den Formaten
- 336 x 280
- 728 x 90
benötigt. Fokus soll hierfür unsere Dienstleistung Onlineshop-Betreuung sein, siehe https://www.kalvorn-beispiel.de/leistungen/shop-betreuung/
Das Design soll sich an den Farben underer Homepage orientieren, ist aber nicht darauf limitiert. Unser Firmenwerte Qualitätsversprechen, Zuverlässigkeit und Transparenz sollen nach Möglichkeit durch das Design ausgedrückt werden, jedoch ohne dabei altbacken / konservativ zu wirken, sondern eine modernen Dienstleister darstellen.
Den genauen Wortlaut / Text für den Banner überlasse ich Ihrer Kreativität, kann sich natürlich an den Texten auf unserer Homepage orientieren.
Das Banner wird gezielt auf bestimmten Webseiten / Blogs eingesetzt werden und auf unsere Homepage verlinkt.
Die Banner müssen auf allen Geräten (mobil bis Desktop) gut lesbar / erkennbar sein.

```html
<!DOCTYPE html>
<html lang="de">
<head>
<meta charset="utf-8">
<title>kalVorn – Onlineshop Betreuung Banner</title>
<link rel="stylesheet" href="https://fonts.googleapis.com/css2?family=Open+Sans:wght@400;600&display=swap">
<style>
  :root {
    --accent-yellow: #f2f54a;
    --brand-grey: #4a5660;
    --blue-deep: #1f97bf;
    --blue-mid: #2fa6cf;
    --blue-light: #63c2e6;
    --white: #ffffff;
    --button-text: #4a5660;
  }
  * { box-sizing: border-box; margin: 0; padding: 0; }
  html, body {
    width: 1200px; height: 769px; overflow: hidden;
    background: var(--white);
    font-family: "Open Sans", Arial, sans-serif;
  }
  .canvas { position: relative; width: 1200px; height: 769px; }

  .wordmark {
    position: absolute;
    color: var(--brand-grey);
    font-weight: 400;
    letter-spacing: 0.5px;
    white-space: nowrap;
    line-height: 1;
  }
  .tick { width: 27px; height: 22px; flex: none; }
  .tick polyline { fill: none; stroke: var(--white); stroke-width: 1.8; }
  .cta {
    position: absolute;
    z-index: 2;
    background: var(--white);
    color: var(--button-text);
    display: flex; align-items: center; justify-content: center; gap: 14px;
    text-decoration: none;
    box-shadow: 0 2px 6px rgba(0,0,0,0.12);
  }
  .cta svg polyline { fill: none; stroke: var(--button-text); stroke-width: 1.6; }

  /* Rectangle format */
  .banner-rect .accent-bar {
    position: absolute; left: 324px; top: 2px; width: 553px; height: 5px;
    background: var(--accent-yellow);
  }
  .banner-rect .wordmark { left: 324px; width: 553px; top: 33px; text-align: center; font-size: 36px; }
  .banner-rect .panel {
    position: absolute; left: 324px; top: 95px; width: 553px; height: 368px;
    background: radial-gradient(ellipse at 42% 40%, var(--blue-light) 0%, var(--blue-mid) 55%, var(--blue-deep) 100%);
    overflow: hidden;
  }
  .banner-rect .panel-head {
    position: absolute; left: 0; top: 0; width: 100%; height: 94px;
    background: var(--blue-deep);
  }
  .banner-rect .title {
    position: absolute; left: 44px; top: 30px;
    color: var(--white); font-weight: 400; font-size: 33px; letter-spacing: 0.4px;
    white-space: nowrap;
  }
  .banner-rect .features { position: absolute; left: 48px; top: 108px; list-style: none; }
  .banner-rect .features li {
    display: flex; align-items: center; gap: 22px;
    color: var(--white); font-size: 25px; height: 43px; white-space: nowrap;
  }
  .banner-rect .cta { left: 644px; top: 388px; width: 233px; height: 58px; font-size: 23px; }

  /* Leaderboard format */
  .banner-wide .accent-bar {
    position: absolute; left: 2px; top: 620px; width: 5px; height: 149px;
    background: var(--accent-yellow);
  }
  .banner-wide .wordmark { left: 7px; width: 220px; top: 676px; text-align: center; font-size: 33px; }
  .banner-wide .title-panel {
    position: absolute; left: 227px; top: 620px; width: 237px; height: 149px;
    background: var(--blue-deep);
    display: flex; align-items: center; justify-content: center;
  }
  .banner-wide .title {
    color: var(--white); font-weight: 400; font-size: 26px; line-height: 1.22;
    text-align: center; letter-spacing: 0.3px;
  }
  .banner-wide .body-panel {
    position: absolute; left: 464px; top: 620px; width: 736px; height: 149px;
    background: linear-gradient(90deg, var(--blue-light) 0%, var(--blue-mid) 55%, var(--blue-deep) 100%);
  }
  .banner-wide .features { position: absolute; left: 28px; top: 8px; list-style: none; }
  .banner-wide .features li {
    display: flex; align-items: center; gap: 20px;
    color: var(--white); font-size: 22px; height: 31.5px; white-space: nowrap;
  }
  .banner-wide .cta { left: 965px; top: 698px; width: 235px; height: 57px; font-size: 23px; }
</style>
</head>
<body>
<main class="canvas">

  <section class="banner banner-rect" aria-label="Banner 336 x 280">
    <div class="accent-bar"></div>
    <div class="wordmark">kalVorn</div>
    <div class="panel">
      <div class="panel-head"><h2 class="title">ONLINESHOP BETREUUNG</h2></div>
      <ul class="features">
        <li><svg class="tick" viewBox="0 0 27 22"><polyline points="1,11 9,21 26,1"/></svg>Full Service Betreuung</li>
        <li><svg class="tick" viewBox="0 0 27 22"><polyline points="1,11 9,21 26,1"/></svg>Analyse und Optimierung</li>
        <li><svg class="tick" viewBox="0 0 27 22"><polyline points="1,11 9,21 26,1"/></svg>SEO Optimierung und Contentpflege</li>
        <li><svg class="tick" viewBox="0 0 27 22"><polyline points="1,11 9,21 26,1"/></svg>Beratung beim Zahlungsverkehr</li>
      </ul>
    </div>
    <a class="cta" href="https://www.kalvorn-beispiel.de/leistungen/shop-betreuung/">Mehr erfahren
      <svg width="12" height="22" viewBox="0 0 12 22"><polyline points="1,1 11,11 1,21"/></svg></a>
  </section>

  <section class="banner banner-wide" aria-label="Banner 728 x 90">
    <div class="accent-bar"></div>
    <div class="wordmark">kalVorn</div>
    <div class="title-panel"><h2 class="title">ONLINESHOP<br>BETREUUNG</h2></div>
    <div class="body-panel">
      <ul class="features">
        <li><svg class="tick" viewBox="0 0 27 22"><polyline points="1,11 9,21 26,1"/></svg>Full Service Betreuung</li>
        <li><svg class="tick" viewBox="0 0 27 22"><polyline points="1,11 9,21 26,1"/></svg>Analyse und Optimierung</li>
        <li><svg class="tick" viewBox="0 0 27 22"><polyline points="1,11 9,21 26,1"/></svg>SEO Optimierung und Contentpflege</li>
        <li><svg class="tick" viewBox="0 0 27 22"><polyline points="1,11 9,21 26,1"/></svg>Beratung beim Zahlungsverkehr</li>
      </ul>
    </div>
    <a class="cta" href="https://www.kalvorn-beispiel.de/leistungen/shop-betreuung/">Mehr erfahren
      <svg width="12" height="22" viewBox="0 0 12 22"><polyline points="1,1 11,11 1,21"/></svg></a>
  </section>

</main>
</body>
</html>
```